Hair salon Business Card

Beauty Salon
I would like to see designs using sky blue and a soft orange. Mainly I would like my name ( Glow N' Wave Salon ) used as the design

Industry/Entity Type

Business

Contact Information for Business Card

Glow N'Wave Salon
418 E Birchfield Hyw #14
San Dimas, Ca 91748
909 527-6184

```html
<!DOCTYPE html>
<html lang="en">
<head>
<meta charset="utf-8">
<title>Glow N' Wave Salon – Business Card</title>
<link rel="stylesheet" href="https://fonts.googleapis.com/css2?family=Oswald:wght@500;700&display=swap">
<style>
  :root {
    --backdrop: #d9dadc;
    --card: #ffffff;
    --sky-blue: #3fb5d2;
    --soft-orange: #f2894f;
    --watermark: #ececec;
    --band-text: #ffffff;
  }
  * { margin: 0; padding: 0; box-sizing: border-box; }
  html, body {
    width: 1200px;
    height: 675px;
    overflow: hidden;
    background: var(--backdrop);
  }
  .business-card {
    position: absolute;
    left: 100px;
    top: 52px;
    width: 1000px;
    height: 571px;
    background: var(--card);
    overflow: hidden;
    box-shadow: 0 6px 24px rgba(0,0,0,0.18);
  }
  .backdrop-words {
    position: absolute;
    left: 40px;
    top: -40px;
    font-family: "Oswald", sans-serif;
    font-weight: 700;
    font-size: 270px;
    line-height: 0.92;
    letter-spacing: 4px;
    color: var(--watermark);
    text-transform: uppercase;
    user-select: none;
  }
  .backdrop-words span { display: block; }
  .salon-name {
    position: absolute;
    left: 0;
    right: 0;
    top: 190px;
    text-align: center;
    font-family: "Oswald", sans-serif;
    font-weight: 500;
    font-size: 130px;
    line-height: 1;
    color: var(--sky-blue);
  }
  .contact-band {
    position: absolute;
    left: 0;
    right: 0;
    bottom: 0;
    height: 64px;
    background: var(--soft-orange);
    display: flex;
    align-items: center;
    justify-content: space-between;
    padding: 0 40px;
    font-family: "Oswald", sans-serif;
    font-weight: 500;
    font-size: 29px;
    color: var(--band-text);
    text-transform: uppercase;
    letter-spacing: 0.5px;
  }
  .contact-item {
    display: flex;
    align-items: center;
    gap: 12px;
  }
  .contact-icon {
    width: 26px;
    height: 26px;
    fill: var(--band-text);
    flex: none;
  }
</style>
</head>
<body>
  <main class="business-card">
    <div class="backdrop-words" aria-hidden="true">
      <span>Beauty</span>
      <span>Salon</span>
    </div>

    <h1 class="salon-name">Glow N' Wave</h1>

    <footer class="contact-band">
      <p class="contact-item address">
        <svg class="contact-icon" viewBox="0 0 24 24" aria-hidden="true">
          <path d="M12 1.5a7.5 7.5 0 0 0-7.5 7.5c0 5.6 7.5 13.5 7.5 13.5s7.5-7.9 7.5-13.5A7.5 7.5 0 0 0 12 1.5zm0 10.3a2.8 2.8 0 1 1 0-5.6 2.8 2.8 0 0 1 0 5.6z"/>
        </svg>
        418 E Birchfield Hyw #14, San Dimas, CA 91748
      </p>
      <p class="contact-item phone">
        <svg class="contact-icon" viewBox="0 0 24 24" aria-hidden="true">
          <path d="M6.6 10.8a15.1 15.1 0 0 0 6.6 6.6l2.2-2.2a1 1 0 0 1 1-.25 11.4 11.4 0 0 0 3.6.57 1 1 0 0 1 1 1V20a1 1 0 0 1-1 1A17 17 0 0 1 3 4a1 1 0 0 1 1-1h3.5a1 1 0 0 1 1 1c0 1.25.2 2.45.57 3.57a1 1 0 0 1-.25 1z"/>
        </svg>
        909 527-6184
      </p>
    </footer>
  </main>
</body>
</html>
```